Website for Corvalind Capital, my new firm that raises money from investors to buy, build, own an...

Corvalind Capital needs a website! We are a new company with very experienced people, who invest in, own and build hotel properties, as well as apartments and other commercial real estate. We seek investors for our projects, and we provide safe, secure returns on their investment in our projects. Our new logo is designed to exhibit strength, class and security, and would like our website to continue on this theme. Our name, Corvalind, is a word-play on a Greek word “aristeia”, which means “excellence” and “a warriors finest moment of glory in war”. If you are in business, you realize that much of it is like war, with strategy and moves and opponents and competitors, and ever-changing economic conditions and threats that make business very much like war. We like to think that we are good at business (war), and so have named our company “Corvalind”, using the founders last name and the word “aristeia” combined. Another definition of "aristeia" is "performing at the peak of one's potential after a long struggle"...again, much like business in real life! The website design should exhibit financial security, smart moves, and positive growth towards a bright future.

Target Market(s)

The target market is smart and wealthy investors, with others such as brokers, cities and government agencies, lenders, sellers, partners, etc also looking at it.

Industry/Entity Type

Investment

Number of Pages Required

5+ page

Font styles to use
Sans Serif

Colors
fec214

Requirements
Must have
• Our website should have a landing page, a "about" or bio page, a projects page and a contact us page. Our new logo uses the colors black and gold, so this should be factored in to our site. The site should be simple, yet impactful and impressive. I have actually two logos, which can be mixed and interchanged in a complimentary way, each with their own unique look.
Nice to have
• I have uploaded a couple screenshots of a website i like, and the simplicity I mention.
Should not have
• The site should not be flashy or complicated or complex or "busy"

```html
<!DOCTYPE html>
<html lang="en">
<head>
<meta charset="utf-8">
<title>Corvalind Capital</title>
<link href="https://fonts.googleapis.com/css2?family=Questrial&display=swap" rel="stylesheet">
<style>
:root{
  --gold:#b68e2f;
  --gold-light:#c99d35;
  --ink:#111111;
  --night:#141a20;
  --grey:#8a8a8a;
  --white:#ffffff;
}
*{box-sizing:border-box;margin:0;padding:0}
html,body{width:1200px;height:2731px;overflow:hidden}
body{position:relative;font-family:"Questrial",sans-serif;color:var(--ink);background:var(--white)}
.abs{position:absolute}
.center{left:0;width:1200px;text-align:center}

/* hero */
.hero{left:0;top:0;width:1200px;height:601px;background:linear-gradient(180deg,#1b1d20 0%,#2a2b2d 45%,#3a3836 80%,#2a2826 100%)}
.brand-name{top:205px;font-size:66px;letter-spacing:6px;color:var(--white)}
.brand-sub{top:285px;font-size:22px;letter-spacing:12px;color:var(--white)}
.tagline{top:418px;font-size:31px;line-height:38px;color:#b9b9b9}
.tagline strong{font-weight:normal;color:#d4d4d4}

/* nav */
.nav{left:0;top:601px;width:1200px;height:54px;background:var(--gold);border-bottom:3px solid #1a1a1a}
.nav a{position:absolute;top:18px;font-size:16px;color:var(--white);text-decoration:none;transform:translateX(-50%)}
.nav-pointer{left:181px;top:643px;width:0;height:0;border-left:9px solid transparent;border-right:9px solid transparent;border-bottom:9px solid #1a1a1a}

/* welcome */
.section-title{font-size:34px;letter-spacing:0.5px}
.section-title span{color:var(--gold)}
.welcome-title{top:716px}
.welcome-text{top:775px;left:162px;width:876px;text-align:center;font-size:13px;line-height:20px;color:var(--grey)}
.btn{display:block;height:53px;font-size:20px;line-height:53px;text-align:left;padding-left:28px}
.btn-dark{left:488px;top:876px;width:200px;background:var(--ink);color:var(--white)}
.btn-light{left:493px;top:2382px;width:200px;height:51px;line-height:51px;background:var(--white);color:var(--ink);padding-left:57px}
.btn-shield{width:48px;height:58px}

/* projects */
.projects{left:0;top:992px;width:1200px;height:569px;background:linear-gradient(160deg,#1f2732 0%,#27313d 40%,#1b222b 75%,#171c22 100%)}
.projects-title{top:1050px;font-size:42px;color:var(--gold)}
.card{width:340px;height:375px;top:1122px}
.card-photo{width:100%;height:249px}
.card-body{height:126px;text-align:center;padding-top:20px}
.card-body h3{font-weight:normal;font-size:29px}
.card-body p{margin-top:12px;font-size:13px;line-height:18px;padding:0 40px}
.card-white .card-body{background:var(--white)}
.card-white h3{color:var(--ink)}
.card-white p{color:#c4c4c4}
.card-gold .card-body{background:var(--gold)}
.card-gold h3{color:var(--white)}
.card-gold p{color:#e6cf97}

/* testimonials */
.testi-title{top:1620px}
.bubble{border:1px solid #d9d9d9;border-radius:3px;text-align:center;background:var(--white)}
.bubble::after{content:"";position:absolute;right:40px;bottom:-12px;width:20px;height:20px;background:var(--white);border-right:1px solid #d9d9d9;border-bottom:1px solid #d9d9d9;transform:rotate(45deg) skew(10deg,10deg)}
.bubble-main{left:422px;top:1692px;width:355px;height:165px;padding:30px 30px;font-size:16px;line-height:21px;color:#6c6c6c}
.bubble-side{width:253px;height:117px;padding:22px 20px;font-size:11px;line-height:14px;color:#dadada;border-color:#eeeeee}
.bubble-side::after{border-color:#eeeeee;width:14px;height:14px;bottom:-8px;right:30px}
.avatar{border-radius:50%;background:radial-gradient(circle at 50% 40%,#e3c9b4 0%,#c49270 55%,#9a7255 100%);border:3px solid #f2f2f2}
.client{text-align:right}
.client-main .c-name{font-size:20px;color:var(--ink)}
.client-main .c-role{font-size:15px;color:#333}
.client-side .c-name{font-size:13px;color:#bdbdbd}
.client-side .c-role{font-size:10px;color:#cfcfcf}
.faded{opacity:0.55}

/* contact */
.contact{left:0;top:2054px;width:1200px;height:441px;background:linear-gradient(180deg,#16222e 0%,#1c2a37 40%,#2a3440 75%,#1d2630 100%)}
.contact-title{top:2112px;font-size:42px;color:var(--gold)}
.contact-text{top:2178px;left:250px;width:700px;text-align:center;font-size:14px;line-height:23px;color:var(--white)}
.field{border:1px solid #d7d7d7;color:var(--white);font-size:13px;padding:9px 12px}

/* footer */
.footer{left:0;top:2495px;width:1200px;height:236px;background:var(--gold)}
.foot-links a{position:absolute;top:2527px;font-size:14px;color:var(--white);text-decoration:none}
.social{top:2510px;width:46px;height:46px;border-radius:50%;border:2px solid #e8d7a8}
.social-dark{background:var(--ink);border-color:var(--ink)}
.foot-rule{left:78px;top:2571px;width:1048px;height:1px;background:#d6bb78}
.foot-info{font-size:13px;line-height:22px;color:#f1e4c2}
.copyright{top:2688px;font-size:13px;color:var(--white)}
.copyright strong{font-size:15px;font-weight:normal;letter-spacing:0.5px}
</style>
</head>
<body>

<header>
  <div class="abs hero" role="img" aria-label="Dark city skyline photograph behind the firm's name"></div>
  <div class="abs center brand-name">CORVALIND</div>
  <div class="abs center brand-sub">CAPITAL</div>
  <p class="abs center tagline"><strong>CORVALIND CAPITAL</strong> provide safe,<br>secure returns on their investment in our projects</p>
  <nav class="abs nav">
    <a href="#" style="left:188px">HOME</a>
    <a href="#" style="left:441px">ABOUT US</a>
    <a href="#" style="left:707px">PROJECTS</a>
    <a href="#" style="left:983px">CONTACT US</a>
  </nav>
  <div class="abs nav-pointer"></div>
</header>

<section class="welcome">
  <h1 class="abs center section-title welcome-title" style="font-weight:normal">WELCOME TO <span>CORVALIND CAPITAL</span></h1>
  <p class="abs welcome-text">Lorem Ipsum is simply dummy text of the printing and typesetting industry. Lorem Ipsum has been the industry's standard dummy text ever since the 1500s, when an unknown printer took a galley of type and scrambled it to make a type specimen book.Lorem Ipsum is simply dummy text of the printing and typesetting industry. Lorem Ipsum has been the industry's standard dummy text ever since the 1500s, when an unknown printer took a galley of type and scrambled it to make a type specimen book.</p>
  <a class="abs btn btn-dark">LEARN MORE</a>
  <svg class="abs btn-shield" style="left:666px;top:873px" viewBox="0 0 48 58" aria-hidden="true">
    <path d="M4 6 L44 6 L44 34 Q44 48 24 56 Q4 48 4 34 Z" fill="var(--gold)"/>
    <path d="M16 29 H31 M25 22 L32 29 L25 36" stroke="#1a1a1a" stroke-width="3" fill="none" stroke-linecap="round"/>
  </svg>
</section>

<section>
  <div class="abs projects" role="img" aria-label="Dark blue photograph of city towers behind the projects"></div>
  <h2 class="abs center projects-title" style="font-weight:normal">PROJECTS</h2>
  <article class="abs card card-white" style="left:77px">
    <div class="card-photo" role="img" aria-label="Photograph of white modern townhouses under mountains" style="background:linear-gradient(180deg,#5f97d6 0%,#9cc0e6 35%,#e8ecef 55%,#b9b9b6 80%,#7f8b5b 100%)"></div>
    <div class="card-body"><h3>Project Name</h3><p>Lorem Ipsum is simply dummy text of the printing and typesetting industry.</p></div>
  </article>
  <article class="abs card card-gold" style="left:430px">
    <div class="card-photo" role="img" aria-label="Photograph of a narrow street with coloured brick houses" style="background:linear-gradient(90deg,#6b5a6c 0%,#8b5b4c 30%,#b58d6c 55%,#8c8a86 75%,#4f5e3e 100%)"></div>
    <div class="card-body"><h3>Project Name</h3><p>Lorem Ipsum is simply dummy text of the printing and typesetting industry.</p></div>
  </article>
  <article class="abs card card-gold" style="left:783px">
    <div class="card-photo" role="img" aria-label="Photograph of a large white apartment building under blue sky" style="background:linear-gradient(180deg,#2f7bd2 0%,#6aa6e6 40%,#e6e8ea 60%,#c9cbc8 82%,#7f8f6a 100%)"></div>
    <div class="card-body"><h3>Project Name</h3><p>Lorem Ipsum is simply dummy text of the printing and typesetting industry.</p></div>
  </article>
</section>

<section>
  <h2 class="abs center section-title testi-title" style="font-weight:normal">WHAT OUR CLIENT <span>SAY ABOUT US</span></h2>

  <div class="faded">
    <div class="abs bubble bubble-side" style="left:109px;top:1717px">Lorem Ipsum is simply dummy text of the printing and typesetting industry. Lorem Ipsum has been the industry's standard dummy text ever since the 1500s.</div>
    <div class="abs client client-side" style="left:150px;top:1877px;width:140px"><div class="c-name">~ Client's Name</div><div class="c-role">Designation</div></div>
    <div class="abs avatar" role="img" aria-label="Client portrait" style="left:297px;top:1857px;width:60px;height:60px"></div>

    <div class="abs bubble bubble-side" style="left:838px;top:1717px">Lorem Ipsum is simply dummy text of the printing and typesetting industry. Lorem Ipsum has been the industry's standard dummy text ever since the 1500s.</div>
    <div class="abs client client-side" style="left:876px;top:1877px;width:140px"><div class="c-name">~ Client's Name</div><div class="c-role">Designation</div></div>
    <div class="abs avatar" role="img" aria-label="Client portrait" style="left:1024px;top:1857px;width:60px;height:60px"></div>
  </div>

  <div class="abs bubble bubble-main">Lorem Ipsum is simply dummy text of the printing and typesetting industry. Lorem Ipsum has been the industry's standard dummy text ever since the 1500s.</div>
  <div class="abs client client-main" style="left:470px;top:1922px;width:200px"><div class="c-name">~ Client's Name</div><div class="c-role">Designation</div></div>
  <div class="abs avatar" role="img" aria-label="Client portrait" style="left:679px;top:1893px;width:100px;height:100px"></div>
</section>

<section>
  <div class="abs contact" role="img" aria-label="Blurred night city photograph behind the contact form"></div>
  <h2 class="abs center contact-title" style="font-weight:normal">KEEP IN TOUCH</h2>
  <p class="abs contact-text">Lorem Ipsum is simply dummy text of the printing and typesetting industry. Lorem Ipsum has been the industry's standard dummy text ever since the 1500s.</p>
  <div class="abs field" style="left:266px;top:2233px;width:331px;height:36px">Name</div>
  <div class="abs field" style="left:603px;top:2233px;width:333px;height:36px">Email Id</div>
  <div class="abs field" style="left:266px;top:2274px;width:670px;height:102px">Comment</div>
  <a class="abs btn btn-light">SUBMIT</a>
  <svg class="abs btn-shield" style="left:673px;top:2378px;width:44px;height:54px" viewBox="0 0 48 58" aria-hidden="true">
    <path d="M4 6 L44 6 L44 34 Q44 48 24 56 Q4 48 4 34 Z" fill="var(--gold)"/>
    <path d="M16 29 H31 M25 22 L32 29 L25 36" stroke="#1a1a1a" stroke-width="3" fill="none" stroke-linecap="round"/>
  </svg>
</section>

<footer>
  <div class="abs footer"></div>
  <div class="foot-links">
    <a href="#" style="left:79px">Home</a>
    <a href="#" style="left:152px">About</a>
    <a href="#" style="left:222px">Projects</a>
    <a href="#" style="left:306px">Contact</a>
  </div>
  <div class="abs social social-dark" style="left:957px" aria-label="Social profile"></div>
  <div class="abs social" style="left:1015px" aria-label="Social profile"></div>
  <div class="abs social" style="left:1073px" aria-label="Social profile"></div>
  <div class="abs foot-rule"></div>

  <svg class="abs" style="left:84px;top:2596px" width="14" height="20" viewBox="0 0 14 20" aria-hidden="true"><path d="M7 0 C3 0 0 3 0 7 C0 12 7 20 7 20 C7 20 14 12 14 7 C14 3 11 0 7 0 Z" fill="#1a1a1a"/><circle cx="7" cy="7" r="2.6" fill="var(--gold)"/></svg>
  <p class="abs foot-info" style="left:108px;top:2593px;width:250px">123, Lorem Ipsum is simply dummy text of the printing and typesetting industry.</p>

  <svg class="abs" style="left:452px;top:2598px" width="18" height="18" viewBox="0 0 18 18" aria-hidden="true"><path d="M4 1 L7 5 L5 7 Q7 11 11 13 L13 11 L17 14 L15 17 Q7 17 1 9 Q1 4 4 1 Z" fill="#1a1a1a"/></svg>
  <p class="abs foot-info" style="left:481px;top:2596px">123 456 7878</p>
  <svg class="abs" style="left:452px;top:2628px" width="18" height="18" viewBox="0 0 18 18" aria-hidden="true"><rect x="1" y="5" width="16" height="12" rx="1" fill="#1a1a1a"/><rect x="4" y="1" width="10" height="5" fill="#1a1a1a"/><rect x="4" y="9" width="10" height="2" fill="var(--gold)"/></svg>
  <p class="abs foot-info" style="left:481px;top:2626px">123 456 7879</p>

  <svg class="abs" style="left:818px;top:2600px" width="20" height="15" viewBox="0 0 20 15" aria-hidden="true"><rect x="1" y="1" width="18" height="13" fill="none" stroke="#1a1a1a" stroke-width="2"/><path d="M1 1 L10 8 L19 1" fill="none" stroke="#1a1a1a" stroke-width="2"/></svg>
  <p class="abs foot-info" style="left:847px;top:2596px">info@corvalind.com</p>
  <svg class="abs" style="left:818px;top:2628px" width="18" height="18" viewBox="0 0 18 18" aria-hidden="true"><circle cx="9" cy="9" r="8" fill="#1a1a1a"/><path d="M1 9 H17 M9 1 Q4 9 9 17 M9 1 Q14 9 9 17" stroke="var(--gold)" stroke-width="1.2" fill="none"/></svg>
  <p class="abs foot-info" style="left:847px;top:2626px">http://www.corvalindcapital.in</p>

  <p class="abs center copyright">© <strong>CORVALIND CAPITAL</strong> - 2018. All Rights Reserved.</p>
</footer>

</body>
</html>
```